Updated Business Card Design more modern and eye catching

looking for something more dynamic than the sterile card we have now. Please take a look at our web site www.brindlemarket.net to see what we do. only looking for the front side of the card for now. I've also attached a sample of a card with raised spot uv ink - it might be cool to incorporate something like that. Card should be bold yet serious. No frilly or scrolly stuff on it.
Updates
Target Market(s)
We do decor and signage for retail business and supermarkets. Our new name should reflect that we're hip but serious.
Contact Information for Business Card
standard business card size - horizontal preferred
Font styles to use
Requirements
Must have
- Current logo and colors cannot be changed.
Nice to have
- Must have information shown on existing card but open to some changes. Okay to consider spot uv.
Should not have
- Not busy with pictures in the background.

```html
<!DOCTYPE html>
<html lang="en">
<head>
<meta charset="utf-8">
<title>Brindle Market – Business Card</title>
<link href="https://fonts.googleapis.com/css2?family=Roboto:wght@400;500;700&display=swap" rel="stylesheet">
<style>
  :root {
    --stage: #d9d6d1;
    --card-dark: #1b1b1d;
    --card-mid: #2a2a2d;
    --gold: #b8ac62;
    --gold-deep: #a89b52;
    --white: #ffffff;
    --ink-soft: #e6e6e6;
    --emboss: #3a3a3e;
  }
  * { margin: 0; padding: 0; box-sizing: border-box; }
  html, body {
    width: 1200px; height: 900px; overflow: hidden;
    background: var(--stage);
    font-family: "Roboto", Arial, sans-serif;
  }
  .card {
    position: absolute; left: 100px; top: 164px;
    width: 1000px; height: 572px;
    background: radial-gradient(ellipse at 40% 30%, var(--card-mid), var(--card-dark) 70%);
    overflow: hidden;
    box-shadow: 0 10px 30px rgba(0,0,0,.25);
  }
  .card-shapes { position: absolute; inset: 0; }
  .brand {
    position: absolute; left: 70px; top: 70px;
    display: flex; align-items: center; gap: 14px;
  }
  .brand-square {
    width: 40px; height: 40px; border: 3px solid var(--gold);
  }
  .brand-name {
    color: var(--gold); font-size: 36px; font-weight: 400;
    letter-spacing: 3px; text-transform: uppercase;
  }
  .person { position: absolute; left: 70px; top: 158px; }
  .person-name {
    font-size: 34px; color: var(--white); font-weight: 400; letter-spacing: 1px;
  }
  .person-name .first { color: var(--gold); font-weight: 700; }
  .person-title { font-size: 22px; color: var(--ink-soft); margin-top: 4px; }
  .person-rule { width: 200px; height: 2px; background: var(--gold); margin-top: 18px; }
  .contact { position: absolute; left: 70px; top: 262px; list-style: none; }
  .contact li {
    display: flex; align-items: center; gap: 16px;
    font-size: 24px; color: var(--white); height: 40px; letter-spacing: .5px;
  }
  .contact svg { width: 26px; height: 26px; fill: var(--gold); flex: none; }
  .contact .ext { color: var(--gold); }
  .address {
    position: absolute; right: 60px; top: 378px;
    text-align: right; color: var(--white); font-size: 23px; line-height: 34px;
    letter-spacing: .5px;
  }
</style>
</head>
<body>
  <div class="card">
    <svg class="card-shapes" width="1000" height="572" viewBox="0 0 1000 572">
      <circle class="uv-circle" cx="770" cy="180" r="138" fill="none" stroke="var(--emboss)" stroke-width="5"/>
      <path class="swoosh-white" d="M0,438 C180,462 420,440 600,372 C430,452 200,478 0,478 Z" fill="var(--white)"/>
      <path class="band-gold" d="M0,490 C230,490 470,450 680,380 C810,338 920,310 1000,292 L1000,572 L0,572 Z" fill="var(--gold)"/>
    </svg>

    <div class="brand">
      <span class="brand-square"></span>
      <span class="brand-name">Brindle Market</span>
    </div>

    <div class="person">
      <div class="person-name"><span class="first">MARTA</span> DELGADO</div>
      <div class="person-title">Vice-President</div>
      <div class="person-rule"></div>
    </div>

    <ul class="contact">
      <li>
        <svg viewBox="0 0 24 24"><path d="M6.6 10.8a15 15 0 0 0 6.6 6.6l2.2-2.2c.3-.3.7-.4 1-.2 1.1.4 2.3.6 3.6.6.6 0 1 .4 1 1V20c0 .6-.4 1-1 1A17 17 0 0 1 3 4c0-.6.4-1 1-1h3.5c.6 0 1 .4 1 1 0 1.3.2 2.5.6 3.6.1.3 0 .7-.2 1z"/></svg>
        <span>561 380 4417 <span class="ext">ext. 3</span></span>
      </li>
      <li>
        <svg viewBox="0 0 24 24"><path d="M7 2h10a2 2 0 0 1 2 2v16a2 2 0 0 1-2 2H7a2 2 0 0 1-2-2V4a2 2 0 0 1 2-2zm0 3v13h10V5zm5 14.2a1 1 0 1 0 0 .01z"/></svg>
        <span>561 902 6638</span>
      </li>
      <li>
        <svg viewBox="0 0 24 24"><path d="M2 5h20v14H2zm2 2v.5l8 5 8-5V7zm0 2.8V17h16V9.8l-8 5z"/></svg>
        <span>martad@brindlemarket.net</span>
      </li>
      <li>
        <svg viewBox="0 0 24 24"><path d="M12 2a10 10 0 1 0 0 20 10 10 0 0 0 0-20zm-1 17.9A8 8 0 0 1 4.2 10.2L9 15v1a2 2 0 0 0 2 2zm6.9-2.5A2 2 0 0 0 16 16h-1v-3a1 1 0 0 0-1-1H8v-2h2a1 1 0 0 0 1-1V7h2a2 2 0 0 0 2-2v-.4a8 8 0 0 1 2.9 12.8z"/></svg>
        <span>www.brindlemarket.net</span>
      </li>
    </ul>

    <div class="address">
      4120 Harbor Trade<br>
      Ct Vero Beach, Fl 32960
    </div>
  </div>
</body>
</html>
```